UK Supplement Company Needs a Label for Diet Protein Powder

We need a new, modern and fresh design for our Diet Protein Powder. Our protein powder is packaged in black plastic tubs (photo attached) and needs an attractive label. We would like to see designs that grab attention and look professional. We're very open to ideas. The label should be 88mm x 365mm. We also prefer PSD format where possible. These alterations could be made once your design is chosen. Have attached photo of our shake ingredients/benefits.
Updates

Need extra days to review

Target Market(s)

Slimmers

Industry/Entity Type

Health And Wellness

Font styles to use
Serif
Sans Serif

Colors

Designer to choose colors to be used in the design.

Requirements
Must have
• Clean, Modern and Professional Look. Eye catching. The flavour, we offer 6 flavours so this must be something we can edit (Flavours are Banana, Chocolate, Chocolate Mint, Strawberry, Toffee and Vanilla).
Nice to have
• Our logo, this can be VORDEL Nutrition or just VORDEL. Our logo files are attached.
Should not have
• We do not want to see people (faces or bodies) on the design.

```html
<!DOCTYPE html>
<html lang="en">
<head>
<meta charset="utf-8">
<title>VORDEL Diet Protein Labels</title>
<link href="https://fonts.googleapis.com/css2?family=Barlow+Condensed:wght@500;600;700&family=Barlow:wght@500;600&display=swap" rel="stylesheet">
<style>
  :root {
    --page: #ffffff;
    --maroon: #6b2436;
    --maroon-deep: #57192b;
    --white: #ffffff;
    --ink: #2a2a2a;
    --fine: #6a6a6a;
    --straw: #ee3338;
    --straw-band: #99191c;
    --straw-badge: #2b2b2b;
    --straw-text: #ffe3e6;
    --lemon: #58a796;
    --lemon-band: #2f6e62;
    --lemon-badge: #a5c84a;
    --lemon-text: #2b6257;
    --grey: #8b8b7d;
    --grey-band: #5e5f56;
    --grey-badge: #a21a1c;
    --grey-text: #2c7472;
  }
  * { box-sizing: border-box; margin: 0; padding: 0; }
  html, body { width: 1200px; height: 717px; overflow: hidden; background: var(--page); }
  .canvas { position: relative; width: 1200px; height: 717px; background: var(--page); }
  .label {
    position: absolute; top: 289px; width: 288px; height: 264px; overflow: hidden;
    font-family: "Barlow Condensed", "Arial Narrow", sans-serif; color: var(--white);
  }
  .label--strawberry { left: 149px; --main: var(--straw); --band: var(--straw-band); --badge: var(--straw-badge); --flav: var(--straw-text); }
  .label--lemon { left: 478px; top: 295px; --main: var(--lemon); --band: var(--lemon-band); --badge: var(--lemon-badge); --flav: var(--lemon-text); }
  .label--plum { left: 795px; top: 286px; --main: var(--grey); --band: var(--grey-band); --badge: var(--grey-badge); --flav: var(--grey-text); }
  .label__pattern {
    position: absolute; left: 0; top: 0; width: 100%; height: 117px;
    background: linear-gradient(135deg, var(--maroon) 0%, var(--maroon-deep) 100%);
  }
  .label__body { position: absolute; left: 0; top: 117px; width: 100%; height: 109px; background: var(--main); }
  .label__band { position: absolute; left: 0; top: 226px; width: 100%; height: 28px; background: var(--band); }
  .brand {
    position: absolute; top: 22px; left: 0; width: 100%; text-align: center;
    font-weight: 700; font-size: 28px; letter-spacing: 0.5px; line-height: 1;
  }
  .title {
    position: absolute; top: 99px; left: 0; width: 100%; text-align: center;
    font-weight: 700; font-size: 37px; letter-spacing: 2px; line-height: 1;
  }
  .subtitle {
    position: absolute; top: 139px; left: 0; width: 100%; text-align: center;
    font-weight: 600; font-size: 15px; color: var(--ink); letter-spacing: 0.3px; line-height: 16px;
  }
  .flavour {
    position: absolute; top: 170px; left: 78px; width: 144px; height: 20px;
    border: 1px solid rgba(40,40,40,0.55); text-align: center; white-space: nowrap;
    font-weight: 600; font-size: 16px; line-height: 18px; color: var(--flav);
  }
  .label--strawberry .flavour { border-color: rgba(255,255,255,0.7); }
  .claim {
    position: absolute; top: 231px; left: 72px; width: 140px; white-space: nowrap;
    font-weight: 600; font-size: 14px; letter-spacing: 1.1px; line-height: 18px;
  }
  .badge {
    position: absolute; top: 203px; left: 218px; width: 46px; height: 51px; background: var(--badge);
    clip-path: polygon(0 14%, 50% 0, 100% 14%, 100% 100%, 0 100%); text-align: center;
  }
  .badge__value { display: block; margin-top: 7px; font-weight: 700; font-size: 20px; line-height: 1; }
  .badge__unit { display: block; font-weight: 700; font-size: 8px; line-height: 1.1; }
  .badge__note { display: block; font-family: "Barlow", Arial, sans-serif; font-size: 6px; line-height: 1.1; opacity: 0.85; }
  .export {
    position: absolute; top: 255px; left: 88px; font-family: "Barlow", Arial, sans-serif;
    font-size: 5px; letter-spacing: 0.5px; color: var(--fine);
  }
</style>
</head>
<body>
<main class="canvas">
  <section class="label label--strawberry">
    <div class="label__pattern" role="img" aria-label="Maroon panel with fine diagonal line pattern"></div>
    <div class="label__body"></div>
    <div class="label__band"></div>
    <p class="brand">VORDEL</p>
    <h1 class="title">DIET PROTEIN</h1>
    <p class="subtitle">POWDER</p>
    <p class="flavour">Strawberry Flavour</p>
    <p class="claim">DIETARY SUPPLEMENT</p>
    <p class="export">FOR EXPORT ONLY</p>
    <div class="badge"><span class="badge__value">117</span><span class="badge__unit">CALORIES</span><span class="badge__note">per serving</span></div>
  </section>
  <section class="label label--lemon">
    <div class="label__pattern" role="img" aria-label="Maroon panel with fine diagonal line pattern"></div>
    <div class="label__body"></div>
    <div class="label__band"></div>
    <p class="brand">VORDEL</p>
    <h2 class="title">DIET PROTEIN</h2>
    <p class="subtitle">POWDER</p>
    <p class="flavour">lemon Flavour</p>
    <p class="claim">DIETARY SUPPLEMENT</p>
    <div class="badge"><span class="badge__value">117</span><span class="badge__unit">CALORIES</span><span class="badge__note">per serving</span></div>
  </section>
  <section class="label label--plum">
    <div class="label__pattern" role="img" aria-label="Maroon panel with fine diagonal line pattern"></div>
    <div class="label__body"></div>
    <div class="label__band"></div>
    <p class="brand">VORDEL</p>
    <h2 class="title">DIET PROTEIN</h2>
    <p class="subtitle">POWDER</p>
    <p class="flavour">IPAUM Flavour</p>
    <p class="claim">DIETARY SUPPLEMENT</p>
    <div class="badge"><span class="badge__value">117</span><span class="badge__unit">CALORIES</span><span class="badge__note">per serving</span></div>
  </section>
</main>
</body>
</html>
```